My website design

It Will be a to-go website for all service requests from the comfort of your home. services ranging from renting an electrician to fix your home electrical issues, DJ for your party, mark-up artist for your wedding and so on. Here are a few websites for inspiration:

https://www.dwellpanel.example/
https://www.chorewren.example/
https://www.gigplover.example/

Number of Pages Required

5+ page

Requirements
Must have
• User's registration form
pros resgistation form
filling out job request form
quotes sent sent back to job requester from various pros within the same zip code
quote accepted
ability to review pros once jobs are completed

```html
<!DOCTYPE html>
<html lang="en">
<head>
<meta charset="utf-8">
<title>Tendwell — Home Maintenance Made Simple</title>
<link href="https://fonts.googleapis.com/css2?family=Poppins:wght@300;400;500;600&family=Raleway:wght@400;500&display=swap" rel="stylesheet">
<style>
:root{
  --green:#3ab54a;
  --green-soft:#eef8ee;
  --ink:#2b3440;
  --text:#555d66;
  --muted:#8a9096;
  --slate:#5b6b73;
  --sky:#f3f8fc;
  --paper:#fafafa;
  --footer:#2a2e38;
  --white:#ffffff;
}
*{margin:0;padding:0;box-sizing:border-box}
html,body{width:1200px;height:3275px;overflow:hidden;background:var(--white)}
body{font-family:"Poppins",sans-serif;color:var(--ink);position:relative}
.abs{position:absolute}
a{color:inherit;text-decoration:none}

/* header + hero */
.hero-photo{left:0;top:0;width:1200px;height:640px;
  background:linear-gradient(100deg,#6b6460 0%,#8a6f66 25%,#3f4a5a 55%,#283445 75%,#8b8d90 100%)}
.hero-shade{left:0;top:0;width:1200px;height:640px;background:rgba(20,28,38,.35)}
.site-header{left:0;top:0;width:1200px;height:83px;background:rgba(255,255,255,.93)}
.brand{font-family:"Poppins",sans-serif;font-weight:500;letter-spacing:9px;font-size:24px;color:var(--ink);display:flex;align-items:center;gap:12px}
.brand-dot{width:18px;height:18px;border-radius:50%;background:var(--green)}
.nav a{position:absolute;top:30px;font-size:15px;font-weight:500;color:var(--ink)}
.nav a.active{color:var(--green);text-decoration:underline}
.nav-caret{left:516px;top:83px;width:0;height:0;border-left:9px solid transparent;border-right:9px solid transparent;border-top:9px solid rgba(255,255,255,.93)}
.btn{display:flex;align-items:center;justify-content:center;background:var(--green);color:var(--white);font-size:15px;font-weight:500;border-radius:2px}
.hero-title{left:0;width:1200px;top:250px;text-align:center;color:var(--white);font-size:45px;font-weight:600;line-height:55px}
.hero-sub{left:0;width:1200px;top:367px;text-align:center;color:var(--white);font-size:19px}
.search{left:357px;top:437px;width:486px;height:45px;border-radius:23px;border:2px solid rgba(255,255,255,.85);display:flex;overflow:hidden}
.search-field{flex:0 0 306px;background:rgba(255,255,255,.18);color:rgba(255,255,255,.7);font-size:16px;display:flex;align-items:center;padding-left:26px;font-family:"Raleway",sans-serif}
.search-go{flex:1;background:var(--white);color:var(--ink);font-weight:500;font-size:16px;display:flex;align-items:center;justify-content:center}
.hero-notch{left:570px;top:610px;width:0;height:0;border-left:30px solid transparent;border-right:30px solid transparent;border-bottom:30px solid var(--green-soft)}

/* services */
.services{left:0;top:640px;width:1200px;height:362px;background:var(--green-soft)}
.section-h{font-size:28px;font-weight:300;color:var(--ink)}
.section-h b{font-weight:600}
.body-copy{font-family:"Raleway",sans-serif;color:var(--ink);font-size:16px;line-height:28px}
.svc{width:174px;text-align:center;font-family:"Raleway",sans-serif;font-size:16px;line-height:21px;color:var(--muted)}
.svc svg{display:block;margin:0 auto 14px}
.svc-active{left:712px;top:735px;width:174px;height:132px;background:var(--slate)}
.svc-active-caret{left:791px;top:867px;width:0;height:0;border-left:8px solid transparent;border-right:8px solid transparent;border-top:8px solid var(--slate)}

/* how it works */
.rule{height:3px;background:var(--green)}
.center-h{left:0;width:1200px;text-align:center}
.step{width:290px;text-align:center}
.step h3{font-size:18px;font-weight:500;color:var(--ink);margin-top:18px}
.step p{font-family:"Raleway",sans-serif;font-size:14.5px;line-height:23px;color:var(--muted);margin-top:16px}
.connector{height:3px;background:var(--green)}

/* intelligence */
.smart{left:0;top:1506px;width:1200px;height:509px;background:var(--sky)}
.family-photo{left:160px;top:1591px;width:289px;height:312px;background:linear-gradient(135deg,#c9d3cd,#9aa7a4 45%,#5d6c7a)}
.brand-card{left:313px;top:1767px;width:189px;height:171px;background:var(--white);box-shadow:0 6px 22px rgba(0,0,0,.08);display:flex;align-items:center;justify-content:center;font-size:22px;font-weight:500;letter-spacing:4px;color:var(--ink)}

/* testimonials */
.reviews{left:0;top:2015px;width:1200px;height:591px;background:var(--paper)}
.card{width:305px;height:289px;background:var(--white);border:1px solid #dfe3e6;padding:0 30px 0 32px}
.avatar{width:64px;height:64px;border-radius:50%;background:linear-gradient(#f1e0cf,#d9b991);margin:24px auto 0}
.card-name{margin-top:20px;font-size:14px;color:var(--ink);display:flex;gap:12px;align-items:center}
.stars{color:#f7a01c;font-size:13px;letter-spacing:1px}
.card p{font-family:"Raleway",sans-serif;font-size:12.4px;line-height:23px;color:var(--text);margin-top:6px}
.card .date{font-family:"Poppins",sans-serif;font-weight:300;font-size:14px;color:var(--muted);margin-top:10px}
.card .tag{font-family:"Raleway",sans-serif;font-size:14px;color:var(--green);margin-top:4px}
.dot{width:10px;height:10px;border-radius:50%;background:#a9dcb0}
.dot.on{width:15px;height:15px;background:var(--green)}

/* cta */
.cta{left:0;top:2606px;width:1200px;height:231px;background:var(--green);overflow:hidden}
.cta-ring{right:-80px;top:-40px;width:300px;height:300px;border-radius:50%;border:60px solid rgba(255,255,255,.07)}
.cta-wedge{left:-30px;top:0;width:140px;height:231px;background:rgba(255,255,255,.06);clip-path:polygon(0 0,40% 0,100% 70%,0 100%)}
.cta h2{font-size:32px;font-weight:600;color:var(--white)}
.cta p{font-size:31px;font-weight:300;color:var(--white)}
.btn-ghost{background:var(--white);color:var(--green);border-radius:23px;font-size:16px;font-weight:500;display:flex;align-items:center;justify-content:center}

/* footer */
.footer{left:0;top:2837px;width:1200px;height:438px;background:var(--footer);color:#c9ccd2}
.footer .brand{color:var(--white)}
.foot-h{font-size:14px;font-weight:500;color:var(--white)}
.foot-links a{display:block;font-size:13.5px;line-height:26.4px;color:#b9bec6}
.foot-small{font-size:13px;line-height:24px;color:#b9bec6}
.subscribe{left:735px;top:3001px;width:347px;height:36px;border-radius:18px;overflow:hidden;display:flex}
.subscribe .field{flex:1;background:#e9edf3;color:#8c939c;font-size:13px;display:flex;align-items:center;padding-left:26px}
.subscribe .go{flex:0 0 118px;background:var(--green);color:var(--white);font-size:14px;font-weight:500;display:flex;align-items:center;justify-content:center}
.social{display:flex;gap:8px}
.social span{width:18px;height:18px;border-radius:50%;background:#5a606c}
.footer-rule{left:0;top:3174px;width:1200px;height:1px;background:#3a3f4a}
</style>
</head>
<body>

<div class="abs hero-photo" role="img" aria-label="Photo of an electrician testing wiring with a multimeter while a homeowner waits on the sofa"></div>
<div class="abs hero-shade"></div>

<header class="abs site-header">
  <div class="abs brand" style="left:117px;top:24px"><span class="brand-dot"></span>TENDWELL</div>
  <nav class="nav">
    <a class="active" style="left:507px">Home</a>
    <a style="left:604px">Services</a>
    <a style="left:704px">Contact</a>
    <a style="left:814px">Login</a>
  </nav>
  <a class="abs btn" style="left:916px;top:19px;width:166px;height:43px">Book A Services</a>
</header>
<div class="abs nav-caret"></div>

<h1 class="abs hero-title">Home Maintenance<br>Made simple</h1>
<p class="abs hero-sub">One Call Can Solve All Your House Problems</p>
<div class="abs search">
  <div class="search-field">What Services do you need</div>
  <div class="search-go">Get Help Today</div>
</div>
<div class="abs hero-notch"></div>
<svg class="abs" style="left:594px;top:626px" width="12" height="8" viewBox="0 0 12 8"><path d="M1 1l5 5 5-5" fill="none" stroke="#3ab54a" stroke-width="1.6"/></svg>

<section class="abs services"></section>
<h2 class="abs section-h" style="left:117px;top:730px">Our <b>Services</b></h2>
<p class="abs body-copy" style="left:117px;top:774px;width:320px">Lorem Ipsum is simply dummy text of the printing and typesetting industry.</p>
<a class="abs btn" style="left:117px;top:845px;width:156px;height:45px">More Services</a>

<div class="abs svc" style="left:518px;top:750px">
  <svg width="50" height="46" viewBox="0 0 50 46" fill="none" stroke="#3ab54a" stroke-width="2"><path d="M8 4v8M16 4v8M5 12h14v8a7 7 0 0 1-14 0z"/><circle cx="33" cy="27" r="11"/><circle cx="33" cy="27" r="5"/><path d="M12 27v8a6 6 0 0 0 12 0"/><path d="M41 38l5 6"/></svg>
  Electrician<br>Services
</div>
<div class="abs svc-active"></div>
<div class="abs svc-active-caret"></div>
<div class="abs svc" style="left:712px;top:750px;color:#fff">
  <svg width="46" height="46" viewBox="0 0 46 46" fill="none" stroke="#fff" stroke-width="1.8"><rect x="3" y="3" width="40" height="40"/><path d="M3 16h40M10 20v18M18 20v18M26 20v18M34 20v18"/><rect x="7" y="26" width="6" height="4"/><rect x="15" y="30" width="6" height="4"/><rect x="23" y="24" width="6" height="4"/><circle cx="37" cy="32" r="4"/><path d="M8 9h30"/></svg>
  DJ For Your<br>Party Services
</div>
<div class="abs svc" style="left:907px;top:750px">
  <svg width="50" height="46" viewBox="0 0 50 46" fill="none" stroke="#3ab54a" stroke-width="2"><circle cx="18" cy="28" r="13"/><circle cx="32" cy="28" r="13"/><path d="M14 12l4-6 4 6M28 12l4-6 4 6"/></svg>
  Mark-Up Artist<br>For Wedding
</div>

<div class="abs rule" style="left:554px;top:1082px;width:64px"></div>
<h2 class="abs center-h" style="top:1103px;font-size:27px;font-weight:500">How Tendwell works</h2>
<p class="abs center-h" style="top:1147px;font-size:21px;font-family:'Raleway',sans-serif;color:var(--text)">Seamless Digital Services At Your Door</p>

<div class="abs connector" style="left:355px;top:1257px;width:150px"></div>
<div class="abs connector" style="left:679px;top:1257px;width:150px"></div>

<div class="abs step" style="left:114px;top:1226px">
  <svg width="96" height="90" viewBox="0 0 96 90" fill="none" stroke="#3ab54a" stroke-width="2.4"><rect x="40" y="4" width="34" height="66" rx="4"/><path d="M48 4v60M74 20h4M74 30h4M74 40h4"/><path d="M40 28H28L10 50v28M40 44H26l-6 10M40 58H30"/></svg>
  <h3>Tell Us How we Can Help</h3>
  <p>Our website makes it easy to tell us<br>what service you need.</p>
</div>
<div class="abs step" style="left:440px;top:1226px">
  <svg width="70" height="90" viewBox="0 0 70 90" fill="none" stroke="#3ab54a" stroke-width="2.4"><path d="M35 88C18 64 3 50 3 33a32 32 0 0 1 64 0c0 17-15 31-32 55z"/><circle cx="35" cy="33" r="20" stroke-dasharray="4 4"/><path d="M35 20v14l9 6"/></svg>
  <h3>Confirm A Time &amp; Location</h3>
  <p>We come to you, whenever you're<br>ready, often in under an hour.</p>
</div>
<div class="abs step" style="left:798px;top:1234px">
  <svg width="86" height="84" viewBox="0 0 86 84" fill="none" stroke="#3ab54a" stroke-width="2.4"><path d="M4 4h78v58H44L30 78V62H4z"/><path d="M28 30h10v22H28zM38 32l8-16c4 0 6 3 5 7l-2 7h11c4 0 5 4 3 6l-3 14H38"/></svg>
  <h3 style="margin-top:10px">Breathe Easy</h3>
  <p>We give you clear, upfront pricing.<br>with cash or credit card. Simple!</p>
</div>

<section class="abs smart"></section>
<div class="abs family-photo" role="img" aria-label="Photo of a smiling family on a sofa looking at a tablet together"></div>
<div class="abs brand-card">TENDWELL</div>
<div class="abs rule" style="left:596px;top:1627px;width:64px"></div>
<h2 class="abs" style="left:597px;top:1650px;font-size:27px;font-weight:500;line-height:41px">Next Generation Home<br>Intelligence Is Here</h2>
<p class="abs" style="left:597px;top:1752px;font-size:21px;font-family:'Raleway',sans-serif;color:var(--ink)">Seamless Digital Services At Your Door</p>
<a class="abs btn" style="left:597px;top:1815px;width:157px;height:45px">Get A Quote</a>

<section class="abs reviews"></section>
<div class="abs rule" style="left:117px;top:2085px;width:64px"></div>
<h2 class="abs section-h" style="left:117px;top:2110px">Don't just take <b>our word for it</b></h2>

<article class="abs card" style="left:117px;top:2193px">
  <div class="avatar" role="img" aria-label="Client portrait"></div>
  <div class="card-name">Client Name <span class="stars">★★★★★</span></div>
  <p>Lorem Ipsum is simply dummy text of the<br>printing and typesetting industry. Lorem<br>Ipsum has been the industry's</p>
  <div class="date">October 11, 2019</div>
  <div class="tag">Electrician Services</div>
</article>
<article class="abs card" style="left:447px;top:2193px">
  <div class="avatar" role="img" aria-label="Client portrait"></div>
  <div class="card-name">Client Name <span class="stars">★★★★★</span></div>
  <p>Lorem Ipsum is simply dummy text of the<br>printing and typesetting industry. Lorem<br>Ipsum has been the industry's</p>
  <div class="date">October 11, 2019</div>
  <div class="tag">Electrician Services</div>
</article>
<article class="abs card" style="left:778px;top:2193px">
  <div class="avatar" role="img" aria-label="Client portrait"></div>
  <div class="card-name">Client Name <span class="stars">★★★★★</span></div>
  <p>Lorem Ipsum is simply dummy text of the<br>printing and typesetting industry. Lorem<br>Ipsum has been the industry's</p>
  <div class="date">October 11, 2019</div>
  <div class="tag">Electrician Services</div>
</article>
<div class="abs" style="left:564px;top:2518px;display:flex;gap:11px;align-items:center">
  <span class="dot"></span><span class="dot on"></span><span class="dot"></span><span class="dot"></span>
</div>

<section class="abs cta">
  <div class="abs cta-wedge"></div>
  <div class="abs cta-ring"></div>
  <h2 class="abs" style="left:122px;top:62px">Ready to getstarted?</h2>
  <p class="abs" style="left:122px;top:110px">A simple way to take care of everything</p>
  <a class="abs btn-ghost" style="left:885px;top:95px;width:197px;height:45px">Book A Services</a>
</section>

<footer class="abs footer">
  <div class="abs brand" style="left:117px;top:106px"><span class="brand-dot"></span>TENDWELL</div>
  <div class="abs" style="left:117px;top:177px;font-size:19px;color:var(--white)">+100 &nbsp;(555-0142)</div>
  <p class="abs foot-small" style="left:117px;top:223px">It's time to Step-up Your Social Media Game<br>and leave your competition behind</p>

  <div class="abs foot-h" style="left:500px;top:96px">Quick Links</div>
  <nav class="abs foot-links" style="left:500px;top:125px">
    <a>Home</a><a>About Us</a><a>Services</a><a>Book A Services</a><a>Site Map</a><a>Contact Us</a>
  </nav>

  <div class="abs foot-h" style="left:732px;top:96px">WRITE TO US</div>
  <div class="abs" style="left:732px;top:131px;font-size:11.5px;color:#b9bec6">Provide your email below to subscribe to our newsletter</div>
  <div class="abs foot-h" style="left:732px;top:222px;font-size:13px">FOLLOW US</div>
  <div class="abs social" style="left:737px;top:254px"><span></span><span></span><span></span><span></span><span></span></div>
  <div class="abs" style="left:0;top:374px;width:1200px;text-align:center;font-size:14px;color:#b9bec6">Copyright 2020 tendwell.example</div>
</footer>
<div class="abs subscribe"><div class="field">Email address</div><div class="go">Subscribe</div></div>
<div class="abs footer-rule"></div>

</body>
</html>
```